R&T Builders and Spaces Business Card

We need to redesign our business card. We had used white vellum wih grey logo and txt in the past. I would like to bring a little life into our cards without being over the top. I think I will be going away from the vellum and printing soft touch business cards.
I have attached what we currently have and our new logo design.

```html
<!DOCTYPE html>
<html lang="en">
<head>
<meta charset="utf-8">
<title>R&amp;T Builders and Spaces – Business Card</title>
<link href="https://fonts.googleapis.com/css2?family=Montserrat:wght@300;400;600&display=swap" rel="stylesheet">
<style>
  :root {
    --ink: #262626;
    --paper: #ffffff;
    --backdrop: #d9d9d9;
    --soft-ink: #e8e8e8;
  }
  * { margin: 0; padding: 0; box-sizing: border-box; }
  html, body { width: 1200px; height: 1200px; overflow: hidden; }
  body {
    background: var(--backdrop);
    font-family: "Montserrat", sans-serif;
    display: flex;
    flex-direction: column;
    align-items: center;
    justify-content: center;
    gap: 50px;
  }
  .card {
    width: 920px;
    height: 526px;
    border-radius: 36px;
    overflow: hidden;
    position: relative;
    box-shadow: 0 10px 30px rgba(0,0,0,0.18);
  }
  .card--front { display: flex; background: var(--paper); }
  .card--back { background: var(--ink); display: flex; align-items: center; justify-content: center; }

  .contact-panel {
    width: 50%;
    background: var(--ink);
    color: var(--paper);
    padding: 150px 0 0 64px;
  }
  .person-name { font-weight: 600; font-size: 40px; letter-spacing: 1px; line-height: 1; }
  .person-role { font-weight: 400; font-size: 24px; letter-spacing: 1px; margin: 6px 0 26px; }
  .contact-list { list-style: none; font-size: 17px; letter-spacing: 0.6px; }
  .contact-list li { display: flex; align-items: flex-start; gap: 12px; margin-bottom: 8px; line-height: 1.3; }
  .contact-list svg { width: 18px; height: 18px; flex: none; margin-top: 2px; fill: var(--paper); }
  .contact-list .inline-icon { margin: 2px 4px 0 10px; }

  .brand-panel {
    width: 50%;
    display: flex;
    align-items: center;
    justify-content: center;
  }
  .brand {
    display: flex;
    flex-direction: column;
    align-items: center;
    gap: 18px;
  }
  .brand-square { width: 150px; height: 150px; }
  .brand-name {
    font-weight: 300;
    font-size: 20px;
    letter-spacing: 2px;
    text-transform: uppercase;
  }
  .brand--dark .brand-square { background: var(--ink); }
  .brand--dark .brand-name { color: var(--ink); }
  .brand--light .brand-square { background: var(--paper); width: 210px; height: 210px; }
  .brand--light .brand-name { color: var(--paper); font-size: 26px; }
</style>
</head>
<body>

  <section class="card card--front">
    <div class="contact-panel">
      <h1 class="person-name">DALE M. HARPER</h1>
      <p class="person-role">PRINCIPAL</p>
      <ul class="contact-list">
        <li>
          <svg viewBox="0 0 24 24"><path d="M6.6 10.8a15 15 0 0 0 6.6 6.6l2.2-2.2a1 1 0 0 1 1-.25 11.4 11.4 0 0 0 3.6.57 1 1 0 0 1 1 1V20a1 1 0 0 1-1 1A17 17 0 0 1 3 4a1 1 0 0 1 1-1h3.5a1 1 0 0 1 1 1c0 1.25.2 2.45.57 3.57a1 1 0 0 1-.25 1z"/></svg>
          <span>555 210 4830</span>
          <svg class="inline-icon" viewBox="0 0 24 24"><path d="M7 1h10a2 2 0 0 1 2 2v18a2 2 0 0 1-2 2H7a2 2 0 0 1-2-2V3a2 2 0 0 1 2-2zm0 3v15h10V4zm5 16.2a.9.9 0 1 0 0 1.8.9.9 0 0 0 0-1.8z"/></svg>
          <span>555 318 7264</span>
        </li>
        <li>
          <svg viewBox="0 0 24 24"><path d="M2 5h20v14H2zm2 2v.3l8 5.4 8-5.4V7zm0 2.7V17h16V9.7l-8 5.4z"/></svg>
          <span>DALEH@RTBUILDERS.COM</span>
        </li>
        <li>
          <svg viewBox="0 0 24 24"><path d="M12 2a10 10 0 1 0 0 20 10 10 0 0 0 0-20zm6.9 6h-3a15 15 0 0 0-1.3-3.9A8 8 0 0 1 18.9 8zM12 4c.8 1.1 1.5 2.5 1.9 4h-3.8c.4-1.5 1.1-2.9 1.9-4zM4.3 14a8 8 0 0 1 0-4h3.4a16 16 0 0 0 0 4zm.8 2h3a15 15 0 0 0 1.3 3.9A8 8 0 0 1 5.1 16zm3-8h-3a8 8 0 0 1 4.3-3.9A15 15 0 0 0 8.1 8zM12 20c-.8-1.1-1.5-2.5-1.9-4h3.8c-.4 1.5-1.1 2.9-1.9 4zm2.3-6H9.7a14 14 0 0 1 0-4h4.6a14 14 0 0 1 0 4zm.3 5.9a15 15 0 0 0 1.3-3.9h3a8 8 0 0 1-4.3 3.9zm1.7-5.9a16 16 0 0 0 0-4h3.4a8 8 0 0 1 0 4z"/></svg>
          <span>WWW.RTBUILDERS.COM</span>
        </li>
        <li>
          <svg viewBox="0 0 24 24"><path d="M12 2a7 7 0 0 0-7 7c0 5.2 7 13 7 13s7-7.8 7-13a7 7 0 0 0-7-7zm0 9.5a2.5 2.5 0 1 1 0-5 2.5 2.5 0 0 1 0 5z"/></svg>
          <span>420 W CANYON RD, STE. 310<br>MESA, ARIZONA 85201</span>
        </li>
      </ul>
    </div>
    <div class="brand-panel">
      <div class="brand brand--dark">
        <div class="brand-square"></div>
        <p class="brand-name">R&amp;T Builders and Spaces</p>
      </div>
    </div>
  </section>

  <section class="card card--back">
    <div class="brand brand--light">
      <div class="brand-square"></div>
      <p class="brand-name">R&amp;T Builders and Spaces</p>
    </div>
  </section>

</body>
</html>
```